Marlow Estate Services (Handyman / Home Improvement Company)

Looking for a double sided professional looking business card with Logo attached to be highlighted on one side and throwing in an image of a handyman as an option would be nice to see as well. We are a company focused on providing quality Handyman and Home improvement services in a timely manner that is done right the first time with integrity

Industry/Entity Type

Handyman / Home Improvement

Contact Information for Business Card

(LOGO, Name, Mobile and office phone numbers, email) on front side of card, (the words "The SOLUTION to all of your Handyman and Home Improvement needs" followed by "Family Owned and Operated" at the very bottom) on the back.

Colors
EB3D1F
EC4F4E
F09395
F8D3D4
FCEDEE

Requirements
Must have
• Red, Gray, Black Color scheme
Should not have
• No Yellow or Blue colors

```html
<!DOCTYPE html>
<html lang="en">
<head>
<meta charset="utf-8">
<title>Marlow Estate Services – Business Card</title>
<link rel="stylesheet" href="https://fonts.googleapis.com/css2?family=Barlow+Condensed:wght@500;600;700&display=swap">
<style>
  :root {
    --red: #e82c2f;
    --black: #111111;
    --ink: #2b2626;
    --white: #ffffff;
    --page: #ffffff;
  }
  * { margin: 0; padding: 0; box-sizing: border-box; }
  html, body { width: 1200px; height: 1200px; overflow: hidden; background: var(--page); }
  body { position: relative; font-family: "Barlow Condensed", sans-serif; }

  .card { position: absolute; left: 266px; width: 677px; height: 388px; overflow: hidden; }
  .card--front { top: 131px; background: var(--white); box-shadow: 0 0 0 1px #eeeeee; }
  .card--back { top: 662px; background: var(--red); }

  .front-wave { position: absolute; left: 0; top: 0; width: 677px; height: 388px; }

  .holder { position: absolute; left: 43px; top: 78px; }
  .holder__name { font-size: 38px; font-weight: 600; color: var(--ink); line-height: 1; }
  .holder__role { font-size: 19px; font-weight: 600; color: var(--red); letter-spacing: 5px; margin-top: 6px; }

  .contacts { position: absolute; left: 43px; top: 157px; list-style: none; }
  .contacts__item { display: flex; align-items: center; height: 35px; margin-bottom: 10px; }
  .contacts__icon { width: 35px; height: 35px; flex: none; }
  .contacts__text { margin-left: 15px; font-size: 29px; font-weight: 500; color: var(--black); line-height: 1; }

  .brand { position: absolute; display: flex; align-items: center; gap: 12px; }
  .brand__mark { width: 22px; height: 22px; border-radius: 50%; background: var(--black); flex: none; }
  .brand__name { font-size: 40px; font-weight: 700; color: var(--red); line-height: 0.95; text-transform: uppercase; }
  .card--front .brand { left: 372px; top: 120px; }
  .card--back .brand { left: 0; right: 0; top: 78px; justify-content: center; }
  .card--back .brand__name { color: var(--white); font-size: 52px; text-align: left; }

  .tagline { position: absolute; left: 0; right: 0; top: 236px; text-align: center; color: var(--white);
             font-weight: 600; font-size: 27px; line-height: 36px; text-transform: uppercase; }
  .tagline__key { color: var(--black); font-size: 35px; }

  .motto { position: absolute; left: 0; right: 0; top: 312px; height: 44px; display: flex; align-items: center; }
  .motto__bar { height: 11px; background: var(--black); }
  .motto__bar--left { width: 145px; }
  .motto__bar--right { flex: 1; }
  .motto__text { padding: 0 12px; font-size: 35px; font-weight: 700; color: var(--black); text-transform: uppercase; white-space: nowrap; }
</style>
</head>
<body>

<section class="card card--front">
  <svg class="front-wave" viewBox="0 0 677 388" aria-hidden="true">
    <path d="M0 335 C60 350 140 360 260 352 C420 340 560 315 677 311 L677 320 C560 326 420 345 250 362 C140 370 50 366 0 356 Z" fill="#111111"/>
    <path d="M0 360 C80 378 170 375 300 362 C440 348 560 331 677 328 L677 388 L0 388 Z" fill="#e82c2f"/>
  </svg>

  <div class="holder">
    <h1 class="holder__name">Dana Whitcombe</h1>
    <p class="holder__role">CEO</p>
  </div>

  <ul class="contacts">
    <li class="contacts__item">
      <svg class="contacts__icon" viewBox="0 0 36 36" aria-hidden="true">
        <circle cx="18" cy="18" r="18" fill="#e82c2f"/>
        <path d="M12 10 l4 0 l1.5 5 l-2.5 2 c1.5 3 3 4.5 6 6 l2-2.5 l5 1.5 l0 4 c-9 1-17-7-16-16z" fill="#fff"/>
      </svg>
      <span class="contacts__text">Your Phone Number</span>
    </li>
    <li class="contacts__item">
      <svg class="contacts__icon" viewBox="0 0 36 36" aria-hidden="true">
        <circle cx="18" cy="18" r="18" fill="#e82c2f"/>
        <path d="M9 15 c0-4 18-4 18 0 l0 2 l-4 0 l0-2 l-10 0 l0 2 l-4 0z" fill="#fff"/>
        <rect x="11" y="18" width="14" height="8" rx="2" fill="#fff"/>
      </svg>
      <span class="contacts__text">Your Phone Office</span>
    </li>
    <li class="contacts__item">
      <svg class="contacts__icon" viewBox="0 0 36 36" aria-hidden="true">
        <circle cx="18" cy="18" r="18" fill="#e82c2f"/>
        <rect x="9" y="12" width="18" height="12" rx="1.5" fill="none" stroke="#fff" stroke-width="2"/>
        <path d="M9.5 12.5 L18 19 L26.5 12.5" fill="none" stroke="#fff" stroke-width="2"/>
      </svg>
      <span class="contacts__text">Your Business Email</span>
    </li>
  </ul>

  <div class="brand">
    <span class="brand__mark" aria-hidden="true"></span>
    <span class="brand__name">Marlow Estate<br>Services</span>
  </div>
</section>

<section class="card card--back">
  <div class="brand">
    <span class="brand__mark" aria-hidden="true"></span>
    <span class="brand__name">Marlow Estate<br>Services</span>
  </div>

  <p class="tagline">Your <span class="tagline__key">Solution</span> to all of your handyman and<br>home improvement needs</p>

  <div class="motto">
    <span class="motto__bar motto__bar--left"></span>
    <span class="motto__text">Family Owned and Operated</span>
    <span class="motto__bar motto__bar--right"></span>
  </div>
</section>

</body>
</html>
```